Explainer Video Landing Page

We will soon have an "explainer" video which will explain to people in a graphical way what it is we do and the solutions we provide. Our current landing page design, located at http://www.relaynetvista.com has a lot of different elements that we like, but won't focus on the new video we have as the "hero". We will want this new landing page to really showcase the video. Some of the other design elements we need are :
1- A link to "Get a Quote Online", in some way. This is the "goal" of the landing page.
2- We'll want some content sections under the video
3- We'll want the lead gen form to be there as well.
As an example, have a look at what BrightOwl did. http://www.brightowl.com/
We like their example, but find it a bit busy. Our design should be cleaner with more whitespace. They are doing a lot of good things on that page that we'll want to mimic, like adding testimonials and existing customer logos.
Thank you in advance for participating in our design project.
Target Market(s)
Small and Mid-size Businesses. This will be a B2B landing page, focused on the communications needs of business.
Look and feel

```html
<!DOCTYPE html>
<html lang="en">
<head>
<meta charset="utf-8">
<title>Veloria – Hosted PBX for Business</title>
<link rel="stylesheet" href="https://fonts.googleapis.com/css2?family=Open+Sans:wght@400;600;700;800&display=swap">
<style>
:root{
  --ink:#333a40;
  --muted:#8a9096;
  --line:#e1e4e7;
  --bg-soft:#eef1f3;
  --orange:#f39200;
  --blue:#1e8fc6;
  --blue-dark:#176f9b;
  --teal:#1ab0a3;
  --pink:#e6147e;
  --yellow:#f5c400;
  --red:#e84b5c;
  --white:#fff;
}
*{box-sizing:border-box;margin:0;padding:0}
html,body{width:1200px;height:2224px;overflow:hidden}
body{font-family:"Open Sans",Arial,sans-serif;color:var(--ink);background:var(--white);font-size:13px;line-height:1.5}
.wrap{width:960px;margin:0 auto;position:relative}

/* header */
.site-header{height:100px}
.site-header .wrap{height:100px}
.brand{position:absolute;left:0;top:30px;display:flex;align-items:center;gap:12px}
.brand-mark{width:30px;height:30px;border-radius:50%;background:var(--ink)}
.brand-name{font-weight:800;font-size:30px;letter-spacing:4px;color:var(--ink)}
.phone{position:absolute;right:0;top:10px;display:flex;align-items:center;gap:6px;font-size:14px;color:var(--ink);font-weight:600}
.main-nav{position:absolute;right:0;top:56px;display:flex;gap:22px}
.main-nav a{font-size:12px;font-weight:700;color:var(--ink);text-decoration:none;text-transform:uppercase}
.main-nav a.active{color:var(--orange);border-bottom:2px solid var(--orange);padding-bottom:4px}

/* hero */
.hero{background:var(--bg-soft);height:500px;padding-top:40px}
.video{width:720px;margin:0 auto;background:#222}
.video-frame{height:400px;background:linear-gradient(135deg,#eae6e0,#cfc9c1 55%,#8c8680);position:relative}
.play{position:absolute;left:50%;top:50%;width:72px;height:50px;margin:-25px 0 0 -36px;background:rgba(20,20,20,.85);border-radius:10px}
.play svg{position:absolute;left:26px;top:14px}
.video-bar{height:30px;background:#1b1b1b;display:flex;align-items:center;padding:0 12px;gap:10px}
.video-bar .track{flex:1;height:6px;background:#444;border-radius:3px;position:relative}
.video-bar .track i{position:absolute;left:0;top:0;height:6px;width:28%;background:var(--blue);border-radius:3px}
.video-bar .hd{background:var(--blue);color:#fff;font-size:10px;font-weight:800;padding:1px 5px}

/* vibe */
.vibe{padding-top:30px;text-align:center;height:380px}
.vibe h2{font-size:13px;font-weight:800;letter-spacing:1px}
.vibe .lead{font-size:11px;color:var(--muted);margin-top:4px}
.features{display:flex;gap:40px;margin-top:30px}
.feature{flex:1;text-align:center}
.feature .icon{height:60px;display:flex;justify-content:center;align-items:center}
.feature h3{font-size:14px;font-weight:700;margin-top:10px}
.feature p{font-size:11px;color:var(--muted);margin:8px 18px 0;line-height:1.6}
.btn{display:inline-block;margin-top:18px;padding:8px 26px;color:#fff;font-size:10px;font-weight:700;text-transform:uppercase;text-decoration:none}
.btn-blue{background:var(--blue-dark)}.btn-orange{background:var(--orange)}.btn-teal{background:var(--teal)}
.c-blue{color:var(--blue)}.c-orange{color:var(--orange)}.c-teal{color:var(--teal)}

/* plans */
.plans{display:flex;height:150px;margin-top:20px}
.plan{flex:1;color:#fff;text-align:center;padding:16px 14px}
.plan-intro{background:var(--pink);display:flex;align-items:center;justify-content:center;font-size:16px;font-weight:800;line-height:1.4;text-transform:uppercase}
.plan-standard{background:var(--yellow)}.plan-extreme{background:var(--red)}.plan-ultimate{background:var(--teal)}
.plan h4{font-size:12px;font-weight:800;text-transform:uppercase}
.plan p{font-size:10px;margin-top:6px;line-height:1.5}
.plan .price{font-size:24px;font-weight:800;margin-top:8px;line-height:1}
.plan .per{font-size:10px;font-weight:600}

/* testimonials + form */
.proof{display:flex;gap:40px;margin-top:40px;height:600px}
.testimonials{flex:1}
.section-title{color:var(--pink);font-size:18px;font-weight:800;text-transform:uppercase;padding-bottom:14px;border-bottom:1px solid var(--line)}
.quotes{display:flex;gap:40px;margin-top:30px}
.quote{flex:1}
.person{display:flex;align-items:center;gap:14px}
.headshot{width:110px;height:110px;border-radius:50%;background:radial-gradient(circle at 50% 40%,#d6c7b8,#8e7e70)}
.person strong{display:block;font-size:16px;color:var(--ink)}
.person span{font-size:11px;color:var(--muted)}
.quote blockquote{margin-top:26px;font-size:11px;color:var(--muted);line-height:1.8;position:relative;padding-left:26px}
.quote blockquote::before{content:"\201C";position:absolute;left:0;top:-14px;font-size:44px;color:var(--ink);font-weight:800}
.demo{width:260px;background:var(--bg-soft);padding:22px}
.demo h3{color:var(--teal);font-size:16px;font-weight:700}
.demo .sub{font-size:13px;font-weight:600}
.demo .note{font-size:10px;color:var(--muted);margin-top:10px;line-height:1.6}
.field{margin-top:12px}
.field label{display:block;font-size:10px;color:var(--muted)}
.field .input{height:28px;background:#fff;border:1px solid var(--line);margin-top:3px}
.field .textarea{height:70px}
.demo .btn{display:block;text-align:center;margin-top:18px;padding:10px}

/* footer */
.footer-links{border-top:1px solid var(--line);margin-top:40px;padding-top:30px;height:340px}
.cols{display:flex}
.col{flex:1}
.col h5{font-size:12px;font-weight:700;margin-bottom:12px}
.col li{list-style:none;font-size:11px;color:var(--muted);line-height:2.1;display:flex;align-items:center;gap:8px}
.col li i{width:14px;height:14px;border-radius:50%;background:var(--muted);display:inline-block}
.bottom-bar{background:var(--bg-soft);height:104px;text-align:center;padding-top:34px;font-size:11px;color:var(--muted);line-height:1.7}
</style>
</head>
<body>

<header class="site-header">
  <div class="wrap">
    <div class="brand"><span class="brand-mark"></span><span class="brand-name">VELORIA</span></div>
    <div class="phone">
      <svg width="14" height="14" viewBox="0 0 24 24"><path fill="#333a40" d="M6.6 10.8a15 15 0 0 0 6.6 6.6l2.2-2.2a1 1 0 0 1 1-.3 11 11 0 0 0 3.6.6 1 1 0 0 1 1 1V20a1 1 0 0 1-1 1A17 17 0 0 1 3 4a1 1 0 0 1 1-1h3.5a1 1 0 0 1 1 1 11 11 0 0 0 .6 3.6 1 1 0 0 1-.3 1z"/></svg>
      1 800 555.0142
    </div>
    <nav class="main-nav">
      <a class="active" href="#">Home</a><a href="#">Plans &amp; Pricing</a><a href="#">Features</a><a href="#">Phones</a><a href="#">Learn More</a><a href="#">Blog</a>
    </nav>
  </div>
</header>

<section class="hero">
  <div class="video">
    <div class="video-frame" role="img" aria-label="Explainer video still: a coffee mug on an office desk">
      <div class="play"><svg width="20" height="22" viewBox="0 0 20 22"><path d="M0 0l20 11L0 22z" fill="#fff"/></svg></div>
    </div>
    <div class="video-bar">
      <svg width="10" height="12" viewBox="0 0 10 12"><path d="M0 0l10 6L0 12z" fill="#ccc"/></svg>
      <div class="track"><i></i></div>
      <span class="hd">HD</span>
    </div>
  </div>
</section>

<main class="wrap">
  <section class="vibe">
    <h2>THE VELORIA VIBE</h2>
    <p class="lead">Check out Veloria's Corporate Culture video to get a sense of the kind of people you'll be working with at Veloria.</p>
    <div class="features">
      <div class="feature">
        <div class="icon"><svg width="56" height="56"><circle cx="28" cy="28" r="26" fill="var(--blue)"/></svg></div>
        <h3 class="c-blue">Is Veloria right for your business?</h3>
        <p>Hear from our clients about how their business grew after switching to a hosted phone system built for teams.</p>
        <a class="btn btn-blue" href="#">Hear our customers</a>
      </div>
      <div class="feature">
        <div class="icon"><svg width="52" height="52" viewBox="0 0 24 24"><path fill="var(--orange)" d="M6.6 10.8a15 15 0 0 0 6.6 6.6l2.2-2.2a1 1 0 0 1 1-.3 11 11 0 0 0 3.6.6 1 1 0 0 1 1 1V20a1 1 0 0 1-1 1A17 17 0 0 1 3 4a1 1 0 0 1 1-1h3.5a1 1 0 0 1 1 1 11 11 0 0 0 .6 3.6 1 1 0 0 1-.3 1z"/></svg></div>
        <h3 class="c-orange">We've got your number, in more than 800 cities.</h3>
        <p>With Veloria, you can port your existing phone number to our hosted PBX system, or choose a new local number.</p>
        <a class="btn btn-orange" href="#">Get a quote online</a>
      </div>
      <div class="feature">
        <div class="icon"><svg width="56" height="56" viewBox="0 0 56 56"><path d="M10 32v-6a18 18 0 0 1 36 0v6" fill="none" stroke="var(--teal)" stroke-width="5"/><rect x="6" y="30" width="10" height="16" rx="3" fill="var(--teal)"/><rect x="40" y="30" width="10" height="16" rx="3" fill="var(--teal)"/></svg></div>
        <h3 class="c-teal">We've got your number, in more than 800 cities.</h3>
        <p>With Veloria, you can port your existing phone number to our hosted PBX system, or choose a new local number.</p>
        <a class="btn btn-teal" href="#">View our plans</a>
      </div>
    </div>
  </section>

  <section class="plans">
    <div class="plan plan-intro">Simple plans<br>to fit your<br>business</div>
    <div class="plan plan-standard"><h4>The Standard</h4><p>Our essential plan with calling and voicemail for every extension.</p><div class="price">$24.50</div><div class="per">month/extension</div></div>
    <div class="plan plan-extreme"><h4>The Extreme</h4><p>Everything in Standard plus call queues and unlimited minutes.</p><div class="price">$24.50</div><div class="per">month/extension</div></div>
    <div class="plan plan-ultimate"><h4>The Ultimate</h4><p>Full unified communications with recording and reporting tools.</p><div class="price">$24.50</div><div class="per">month/extension</div></div>
  </section>

  <section class="proof">
    <div class="testimonials">
      <h2 class="section-title">Testimonials</h2>
      <div class="quotes">
        <div class="quote">
          <div class="person"><div class="headshot" role="img" aria-label="Headshot of Daniel Reeve"></div><div><strong>Daniel Reeve</strong><span>Business phone solutions</span></div></div>
          <blockquote>Switching our office to hosted phones was easier than we expected. Setup took one afternoon, our numbers moved over without a hitch, and the support team answered every question quickly. Our staff now take calls from anywhere, and our monthly bill dropped noticeably. We would recommend the service to any growing business looking for reliable calling.</blockquote>
        </div>
        <div class="quote">
          <div class="person"><div class="headshot" role="img" aria-label="Headshot of Marcus Hale"></div><div><strong>Marcus Hale</strong><span>Business phone solutions</span></div></div>
          <blockquote>We run three small offices and needed one phone system for all of them. The plans are clear, the pricing is fair, and call quality has been excellent from day one. Adding new extensions takes minutes. Our customers reach the right person faster, and our team finally spends less time managing phones and more time serving clients.</blockquote>
        </div>
      </div>
    </div>
    <aside class="demo">
      <h3>Not Sure?</h3>
      <p class="sub">Sign Up for a Personalized Demo</p>
      <p class="note">A member of our team will walk you through the system, answer your questions and show how hosted PBX fits your business. Call 1 800 555.0142 to speak to someone now.</p>
      <div class="field"><label>First Name *</label><div class="input"></div></div>
      <div class="field"><label>Last Name *</label><div class="input"></div></div>
      <div class="field"><label>Email *</label><div class="input"></div></div>
      <div class="field"><label>Phone *</label><div class="input"></div></div>
      <div class="field"><label>Comments</label><div class="input textarea"></div></div>
      <a class="btn btn-orange" href="#">Request a demo</a>
    </aside>
  </section>

  <footer class="footer-links">
    <div class="cols">
      <div class="col"><h5>Features &amp; Benefits</h5><ul><li>Included Features</li><li>Optional Features</li><li>Conferencing</li><li>Can I Keep My Number?</li><li>Hosted VoIP Phones</li><li>Money Back Guarantee</li></ul></div>
      <div class="col"><h5>Resources</h5><ul><li>What is Hosted PBX</li><li>Frequently Asked Questions</li><li>Testimonials</li><li>VoIP Glossary</li><li>Dashboard</li></ul></div>
      <div class="col"><h5>Veloria</h5><ul><li>Contact Us</li><li>Media Resources</li><li>Our History</li><li>Jobs</li><li>Veloria Vibe</li><li>Cost Of Ownership</li></ul></div>
      <div class="col"><h5>Social</h5><ul><li><i></i>Pagebook</li><li><i></i>Chirpline</li><li><i></i>Clipstream</li><li><i></i>Circleplus</li><li><i></i>Linkwork</li></ul></div>
    </div>
  </footer>
</main>

<div class="bottom-bar">
  Call 1 800 555.0142 or email hello@veloria.com<br>
  Copyright © 2014 Veloria. All rights reserved. This site has a privacy policy.
</div>

</body>
</html>
```